Black Car Limousine transportation business in Naples Florida

Steadfast stand for my reliability and RNT stands for Rest, N and T are the first initials of my children's names. It should show professionalism and a dedication to customer service. We keep our clients identities private. Show our professionalism. We are Black car Black tie company. We service transportation on a reserve basis to and from residents, airports, casinos, hotels,

Target Market(s)

It is a Private car service. High end clients. Businesses, Celebrity and athletes. Service to airports, hotels, special events.

Industry/Entity Type

Business

Contact Information for Business Card

A pearl metallic or Luster card. Standard business card size. Would like the name, Company email, show we take credit cards and phone number. Currently I don't have a website but will like to add later.

Logo Text

STEADFAST RNT TRANSPORTATION

Font styles to use
Serif

Colors
eaeaea
000000

Requirements
Must have
• Must have Company email, show we take credit cards and phone number. Currently I don't have a website but will like to add later.
Nice to have
• Would like to stay with a black and white theme. Open to some color trim.
Should not have
• Open to suggestions

```html
<!DOCTYPE html>
<html lang="en">
<head>
<meta charset="utf-8">
<title>Steadfast RNT Transportation – Business Card</title>
<link href="https://fonts.googleapis.com/css2?family=Lora:wght@400&display=swap" rel="stylesheet">
<style>
  :root{
    --bg:#2a2622;
    --card-black:#050505;
    --card-back:#161616;
    --text-light:#eaeaea;
    --text-muted:#b8b8b8;
    --photo-dark:#0d0d0d;
    --photo-mid:#3a3a3a;
    --photo-high:#5a5a5a;
  }
  *{margin:0;padding:0;box-sizing:border-box}
  html,body{width:1200px;height:1020px;overflow:hidden;background:var(--bg)}
  body{font-family:"Lora",Georgia,serif;color:var(--text-light);position:relative}

  .card{position:absolute;left:180px;width:840px;height:480px;overflow:hidden}
  .card--back{top:20px;background:linear-gradient(120deg,#2c2c2c 0%,var(--card-back) 35%,#080808 100%)}
  .card--front{top:520px;background:var(--card-black)}

  .photo{position:absolute}
  .card--back .photo{left:200px;top:0;width:640px;height:400px;
    background:
      radial-gradient(ellipse 45% 40% at 62% 48%,var(--photo-high) 0%,var(--photo-mid) 35%,transparent 75%),
      linear-gradient(90deg,transparent 0%,#1e1e1e 30%,#1a1a1a 80%,#0c0c0c 100%);}
  .card--front .photo{left:260px;top:0;width:580px;height:480px;
    background:
      radial-gradient(ellipse 42% 38% at 58% 52%,var(--photo-high) 0%,var(--photo-mid) 40%,transparent 78%),
      radial-gradient(ellipse 60% 55% at 58% 55%,#242424 0%,var(--photo-dark) 80%),
      linear-gradient(90deg,var(--card-black) 0%,transparent 30%);}

  .logo{position:absolute;color:var(--text-light);font-weight:400;line-height:1}
  .logo span{display:block}
  .logo__sub{letter-spacing:.42em}
  .card--back .logo{left:60px;top:250px;color:#d2d2d2}
  .card--back .logo__top{font-size:34px;margin-left:4px}
  .card--back .logo__main{font-size:86px;margin:2px 0 8px}
  .card--back .logo__sub{font-size:22px}
  .card--front .logo{left:150px;top:40px;text-align:center}
  .card--front .logo__top{font-size:18px}
  .card--front .logo__main{font-size:46px;margin:0 0 6px}
  .card--front .logo__sub{font-size:13px}

  .person{position:absolute;left:80px;top:180px;border-left:5px solid var(--text-light);padding-left:12px}
  .person__name{font-size:30px;line-height:1.1}
  .person__title{font-size:17px;color:var(--text-muted)}

  .contact{position:absolute;left:80px;top:285px;list-style:none}
  .contact li{display:flex;align-items:center;gap:14px;font-size:19px;margin-bottom:20px}
  .contact svg{width:22px;height:18px;flex:none}

  .payments{position:absolute;left:80px;top:410px;display:flex;align-items:center;gap:10px;font-size:15px;color:var(--text-muted)}
  .payments svg{width:34px;height:22px;flex:none}
</style>
</head>
<body>
  <section class="card card--back">
    <div class="photo" role="img" aria-label="Rear view photograph of a black luxury SUV"></div>
    <div class="logo">
      <span class="logo__top">Steadfast</span>
      <span class="logo__main">RNT</span>
      <span class="logo__sub">TRANSPORTATION</span>
    </div>
  </section>

  <section class="card card--front">
    <div class="photo" role="img" aria-label="Front view photograph of a black luxury SUV"></div>
    <div class="logo">
      <span class="logo__top">Steadfast</span>
      <span class="logo__main">RNT</span>
      <span class="logo__sub">TRANSPORTATION</span>
    </div>
    <div class="person">
      <p class="person__name">Daniel Moreau</p>
      <p class="person__title">Job Title</p>
    </div>
    <ul class="contact">
      <li>
        <svg viewBox="0 0 22 18" aria-hidden="true" fill="#eaeaea"><path d="M2 6c0-3 4-5 9-5s9 2 9 5v2h-5V6c-1-1-7-1-8 0v2H2z"/><rect x="4" y="9" width="14" height="8" rx="1"/></svg>
        <span>(877) 555-0142</span>
      </li>
      <li>
        <svg viewBox="0 0 22 18" aria-hidden="true"><path d="M1 2h20v14H1z" fill="none" stroke="#eaeaea" stroke-width="2"/><path d="M1 2l10 8 10-8" fill="none" stroke="#eaeaea" stroke-width="2"/></svg>
        <span>steadfastrnttransportation@mail.com</span>
      </li>
    </ul>
    <div class="payments">
      <svg viewBox="0 0 34 22" aria-hidden="true"><rect x="1" y="1" width="32" height="20" rx="3" fill="none" stroke="#eaeaea" stroke-width="2"/><rect x="1" y="6" width="32" height="4" fill="#eaeaea"/><rect x="5" y="14" width="10" height="3" fill="#eaeaea"/></svg>
      <span>All major credit cards accepted</span>
    </div>
  </section>
</body>
</html>
```